U.S. Popcorn company needs business cards

We are a popcorn company that manufactures popcorn and sells it to grocery stores worldwide. Our theme is "Americana" and our logo is U.S. route 66 which is the most famous highway in the U.S.

We would like the design to be simple and to use both sides. On the back side we would like to see just the logo and website. The front would be normal details

Target Market(s)

Wholesalers, grocers and distributors

Industry/Entity Type

Manufacture

Contact Information for Business Card

Business name: Bluebell Ridge Popcorn
Phone: +1 555 014 2286
Email: Derek@bluebellridgepopcorn.com
website: www.bluebellridgepopcorn.com
Tag Line: "Freshly popped daily"
Name: Derek Halvorsen
Title: Founder/President

Requirements
Must have
• Either this design should be fun or clean and simple. I will let you show me your thougths.
Nice to have
• Anything that ties in the real Hwy Route 66.
• Colors might need to be red, white and blue incorporated.
Should not have
• Not be too busy.

```html
<!DOCTYPE html>
<html lang="en">
<head>
<meta charset="utf-8">
<title>Bluebell Ridge Popcorn – Business Cards</title>
<link rel="stylesheet" href="https://fonts.googleapis.com/css2?family=Open+Sans:wght@400;600;700&family=EB+Garamond:ital@1&display=swap">
<style>
  :root {
    --backdrop: #181818;
    --royal: #0a3cb4;
    --royal-deep: #051c6e;
    --navy: #0f2a78;
    --paper: #f4f3f5;
    --white: #ffffff;
    --red: #e3202f;
    --silver: #c9c9c9;
  }
  html, body {
    margin: 0;
    width: 1200px;
    height: 900px;
    overflow: hidden;
    background: var(--backdrop);
    font-family: "Open Sans", Arial, sans-serif;
  }
  .canvas { position: relative; width: 1200px; height: 900px; }
  .card {
    position: absolute;
    top: 170px;
    width: 347px;
    height: 561px;
    overflow: hidden;
  }
  .card--front { left: 237px; }
  .card--back {
    left: 649px;
    background: linear-gradient(180deg, var(--white) 0%, #e6e6e6 25%, var(--silver) 52%, #e8e8e8 78%, var(--white) 100%);
  }
  .band {
    position: absolute; left: 0; width: 100%;
    color: var(--white); text-align: center;
  }
  .band--top {
    top: 0; height: 154px;
    background: linear-gradient(180deg, var(--royal-deep) 0%, #0a2fa0 35%, var(--royal) 100%);
  }
  .band--middle { top: 154px; height: 233px; background: var(--paper); color: var(--navy); }
  .band--bottom {
    top: 387px; height: 174px;
    background: linear-gradient(180deg, var(--royal) 0%, #0a36a8 45%, var(--royal-deep) 100%);
  }
  .holder-name {
    margin: 0; position: absolute; top: 53px; width: 100%;
    font-size: 22px; font-weight: 600; letter-spacing: 0.5px;
  }
  .holder-title {
    margin: 0; position: absolute; top: 81px; width: 100%;
    font-size: 16px; font-weight: 400;
  }
  .brand {
    position: absolute; left: 0; width: 100%;
    display: flex; align-items: center; justify-content: center; gap: 10px;
    color: var(--navy); font-weight: 700;
  }
  .brand-dot { display: block; border-radius: 50%; background: var(--red); flex: none; }
  .band--middle .brand { top: 72px; font-size: 20px; }
  .band--middle .brand-dot { width: 16px; height: 16px; }
  .tagline {
    position: absolute; top: 181px; width: 100%; margin: 0;
    font-family: "EB Garamond", Georgia, serif; font-style: italic;
    font-size: 17px; letter-spacing: 0.6px; color: var(--navy);
  }
  .contact {
    position: absolute; top: 52px; width: 100%;
    margin: 0; padding: 0; list-style: none;
    font-size: 17px; line-height: 25.5px;
  }
  .card--back .brand {
    top: 238px; flex-direction: column; gap: 14px; font-size: 25px;
  }
  .card--back .brand-dot { width: 34px; height: 34px; }
</style>
</head>
<body>
<div class="canvas">
  <section class="card card--front" aria-label="Business card front">
    <div class="band band--top">
      <h1 class="holder-name">DEREK HALVORSEN</h1>
      <p class="holder-title">Founder/President</p>
    </div>
    <div class="band band--middle">
      <div class="brand"><span class="brand-dot"></span>Bluebell Ridge Popcorn</div>
      <p class="tagline">FRESHLY POPPED DAILY</p>
    </div>
    <div class="band band--bottom">
      <ul class="contact">
        <li>+1 555 014 2286</li>
        <li>Derek@bluebellridgepopcorn.com</li>
        <li>www.bluebellridgepopcorn.com</li>
      </ul>
    </div>
  </section>

  <section class="card card--back" aria-label="Business card back">
    <div class="brand"><span class="brand-dot"></span>Bluebell Ridge Popcorn</div>
  </section>
</div>
</body>
</html>
```